Electrical contractor

looking for a standard sized, horizontal, double sided business card for an electrical contractors business.
i have played around on microsoft word (only computer program i know how to use!) and will attach what i have made so far, really open to any ideas. i just want the ROFT to stand out to the rest of the business name.

i wish to use the colours black and green, and white for writing. i will attach the pictures i took off google, i want to either use them, or somethin similar for the back grounds

i wish the front to have the following info:
business name: R.O.F.T ELECTRICAL CONTRACTORS
MY NAME; DARREN HOLT
STATUS; A CLASS ELECTRICIAN
LICENSE NO; TRK784150
PH NO. 0437615942
EMAIL ADD. ROFT.ELECTRICAL@VOLTMAILBOX.COM
AND MY SLOGAN: where excellence meets integrity, and service comes with a smile.

i am not sure what to have on the back, other than what i do for work.eg titled WHAT WE DO
i dont want too much written on there or will look crowded, but options to add to back, from most important to least, please pick however many you think will look the best
new homes/extentions
led lighting and downlights
Solar Power
power
safety switches
switchboards
telephone and tv
smoke alarms
stoves and ovens
hot water systems
fault finding
re wiring
Updates

Thank you to those who have submitted designs, I would like to change my slogan to something more simple, I'm thinking something like. RELIABLE. EFFICIENT. PROFESSIONAL. AFFORDABLE. in what ever order you thinks fits best. Thanks

```html
<!DOCTYPE html>
<html lang="en">
<head>
<meta charset="utf-8">
<title>R.O.F.T Electrical Contractors – Business Card</title>
<link rel="stylesheet" href="https://fonts.googleapis.com/css2?family=Arimo:wght@400;700&family=Montserrat:wght@700&family=Questrial&display=swap">
<style>
  :root {
    --card-bg: #0d1112;
    --brand-green: #4dc43b;
    --corner-green: #2a8a0f;
    --corner-mid: #1f5c12;
    --text-white: #ffffff;
  }
  html, body {
    margin: 0;
    padding: 0;
    width: 1200px;
    height: 695px;
    overflow: hidden;
    background: var(--card-bg);
  }
  .card {
    position: relative;
    width: 1200px;
    height: 695px;
    background: var(--card-bg);
    overflow: hidden;
    font-family: "Arimo", Arial, sans-serif;
  }
  .corner { position: absolute; display: block; }
  .corner--top-left { left: 0; top: 0; }
  .corner--bottom-right { right: 0; bottom: 0; }

  .business-name {
    position: absolute;
    left: 0;
    width: 1220px;
    top: 122px;
    margin: 0;
    text-align: center;
    font-family: "Montserrat", Arial, sans-serif;
    font-weight: 700;
    font-size: 52px;
    line-height: 1;
    letter-spacing: 0.6px;
    color: var(--text-white);
    white-space: nowrap;
  }
  .business-name__initials { color: var(--brand-green); }

  .slogan {
    position: absolute;
    left: 40px;
    width: 1140px;
    top: 213px;
    margin: 0;
    text-align: center;
    font-family: "Questrial", Arial, sans-serif;
    font-size: 34px;
    line-height: 1;
    letter-spacing: 1px;
    color: var(--brand-green);
    white-space: nowrap;
  }

  .contact-line {
    position: absolute;
    left: 53px;
    margin: 0;
    font-size: 43px;
    line-height: 1;
    color: var(--text-white);
    white-space: nowrap;
  }
  .contact-line--name { top: 413px; left: 50px; color: var(--brand-green); }
  .contact-line__status {
    font-size: 24px;
    color: var(--text-white);
    margin-left: 22px;
    letter-spacing: 1px;
  }
  .contact-line--license { top: 486px; }
  .contact-line--phone { top: 557px; }
  .contact-line--email { top: 625px; left: 50px; font-size: 42px; }

  .bulb-icon-area {
    position: absolute;
    left: 793px;
    top: 285px;
    width: 250px;
    height: 366px;
    border-radius: 50% 50% 40% 40%;
    background: radial-gradient(ellipse at 50% 45%, rgba(77,196,59,0.55) 0%, rgba(77,196,59,0.25) 45%, rgba(13,17,18,0) 72%);
  }
</style>
</head>
<body>
  <main class="card">
    <svg class="corner corner--top-left" width="230" height="171" viewBox="0 0 230 171" aria-hidden="true">
      <defs>
        <linearGradient id="cornerFadeTop" x1="0" y1="0" x2="1" y2="1">
          <stop offset="0" stop-color="var(--corner-green)"/>
          <stop offset="0.55" stop-color="var(--corner-mid)"/>
          <stop offset="1" stop-color="var(--card-bg)"/>
        </linearGradient>
      </defs>
      <polygon points="0,0 230,0 0,171" fill="url(#cornerFadeTop)"/>
    </svg>

    <svg class="corner corner--bottom-right" width="194" height="160" viewBox="0 0 194 160" aria-hidden="true">
      <defs>
        <linearGradient id="cornerFadeBottom" x1="1" y1="1" x2="0" y2="0">
          <stop offset="0" stop-color="var(--corner-green)"/>
          <stop offset="0.55" stop-color="var(--corner-mid)"/>
          <stop offset="1" stop-color="var(--card-bg)"/>
        </linearGradient>
      </defs>
      <polygon points="194,0 194,160 0,160" fill="url(#cornerFadeBottom)"/>
    </svg>

    <h1 class="business-name"><span class="business-name__initials">R.O.F.T</span> ELECTRICAL CONTRACTORS</h1>
    <p class="slogan">“reliable. efficient. professional. affordable.”</p>

    <p class="contact-line contact-line--name">DARREN HOLT<span class="contact-line__status">A CLASS ELECTRICIAN</span></p>
    <p class="contact-line contact-line--license">LICENSE NO: trk784150</p>
    <p class="contact-line contact-line--phone">PH: 0437615942</p>
    <p class="contact-line contact-line--email">EMAIL: roft.electrical@voltmailbox.com</p>

    <div class="bulb-icon-area" role="img" aria-label="Green light bulb icon with a lightning bolt inside and rays above"></div>
  </main>
</body>
</html>
```